DebtHarbor.com website design

We are a collection agency that collects debt from past residents of apartments on behalf of Property Management Companies. We are want to design a 3 page website with - Home - How it Works - Schedule Demo. We'd like a sketch of a skyline showing high rise apartment buildings, houses, shops, etc. We would like for there to be some animation, possibly clouds and the sun slowly moving. Maybe kids playing ball or catch or something like that. Bird flying and landing. An electric car charging (to indicate we are modern). We are looking for a friendly community vibe. The site will also need a button "Property Managers Login". When some comes to the site we would like a pop up that says "Property Managers Click Here/Past Residents Click Here" with a different icon for each that relates to the description. I've included a link to a test site we had designed so feel free to use some of the copy from it. We just aren't happy with the design. On the Home page our tag line should be "Get more payments, faster, from past residents!" and "Digital First, NOT Digital Only". All without transaction fees, we don't get paid unless we get you paid first!
Additional selling points:

24 hour virtual agent and virtual telephone agent so we don't miss any opportunities to GET YOUR MONEY!

Old school collection strategies meet cutting edge technology to create effective work flow algorithms to put the best debt collectors on your accounts with data driven intelligence to determine the best way to get paid.

No Subscription Fees
No Payment Processing Fees
No Software Fees
No Mail, Email or TXT Fees

Inquire about our FIRST PARTY accounts receivable outsourcing. You may qualify for free post move out A/R processing and AI payment negotiator for the low hanging fruit. Don't pay full collection commission when there wasn't a full collection attempt!

For the How it Works page - See the page from our previous design. I will include the link below. Please come up with your own version of this but you can use the copy from this page.

The schedule demo page will be a form that will feed to our CRM that will include:
Name
Email
Company
Title
Phone Number
Number of Units
Tell us how we can help you: (a box for them provide details)

Also include our phone number at the bottom with something like

Here is a link to our previous design test site:
https://brisklane-preview.net/debtharbor-new/
I've attached an image of the back end so you can get an idea of the colors we need, I've also included our logo. For the most part we would like most of the site to match the blue colors from our logo, but we do need to incorporate some of the yellow in the images I've attached. Possibly make the buttons on the site the yellow color? Make the sun Match the yellow? I'll leave it up to you.

```html
<!DOCTYPE html>
<html lang="en">
<head>
<meta charset="utf-8">
<title>How It Works – DebtHarbor</title>
<link href="https://fonts.googleapis.com/css2?family=Lato:wght@400;700;900&display=swap" rel="stylesheet">
<style>
:root{
  --navy:#1d2c6b;
  --navy-btn:#1a3a78;
  --teal:#1a9fb5;
  --muted:#8d93b8;
  --badge:#e9ebf1;
  --ink-dark:#222222;
  --card-dark:#2e2e2e;
  --circle-gray:#6b6b6b;
  --amber:#f6b563;
  --white:#ffffff;
  --line:#9aa0c0;
}
*{box-sizing:border-box;margin:0;padding:0}
html,body{width:1200px;height:4148px;overflow:hidden}
body{position:relative;font-family:'Lato',sans-serif;background:var(--white);color:var(--navy)}
.abs{position:absolute}

/* header */
.brand{left:84px;top:22px;display:flex;align-items:center;gap:10px}
.brand-dot{width:36px;height:36px;border-radius:50%;background:var(--teal)}
.brand-name{font-size:26px;font-weight:900;color:var(--navy);letter-spacing:-.3px}
.nav{top:32px;left:484px;display:flex;gap:34px;font-size:13px;color:var(--muted)}
.nav .active{color:var(--navy);font-weight:700}
.btn-login{left:830px;top:22px;width:84px;height:38px;border:2px solid var(--navy-btn);color:var(--navy-btn);font-size:13px;font-weight:700;display:flex;align-items:center;justify-content:center}
.btn-pm{left:925px;top:22px;width:192px;height:38px;background:var(--navy-btn);color:var(--white);font-size:13px;font-weight:700;display:flex;align-items:center;justify-content:center}

/* intro */
.page-title{top:164px;width:1200px;text-align:center;font-size:46px;font-weight:700;color:#1a1f3a}
.page-sub{top:236px;width:1200px;text-align:center;font-size:19px;color:var(--muted)}

/* steps */
.connectors{left:0;top:0}
.photo{width:333px;height:283px;border-radius:10px}
.node{width:60px;height:60px;border-radius:50%;background:var(--white);box-shadow:0 4px 14px rgba(29,44,107,.15);display:flex;align-items:center;justify-content:center;transform:translate(-50%,-50%)}
.node span{width:22px;height:22px;border-radius:50%;border:3px solid var(--teal)}
.step-text{width:600px}
.badge{display:inline-block;background:var(--badge);color:var(--navy);font-size:12px;font-weight:700;padding:12px 19px;margin-bottom:22px}
.step-title{font-size:34px;font-weight:700;line-height:1.2;color:var(--navy);letter-spacing:-.4px;margin-bottom:14px}
.step-body{font-size:12.5px;line-height:1.6;color:var(--muted);width:570px}

/* painless */
.dark{left:0;top:2948px;width:1200px;height:1200px;background:var(--ink-dark)}
.dark-title{top:3026px;width:1200px;text-align:center;font-size:40px;font-weight:700;color:var(--white)}
.dark-lead{top:3097px;left:250px;width:700px;text-align:center;font-size:13.5px;line-height:1.75;color:#d8d8d8}
.card{top:3238px;width:331px;height:330px;background:var(--card-dark);display:flex;flex-direction:column;align-items:center;padding-top:30px}
.card-icon{width:120px;height:120px;border-radius:50%;background:var(--circle-gray);display:flex;align-items:center;justify-content:center}
.card-text{margin-top:34px;width:250px;text-align:center;font-size:19px;font-weight:700;line-height:1.4;color:var(--white)}
.btn-start{left:513px;top:3623px;width:174px;height:49px;background:var(--white);color:#1a1a1a;font-size:14px;font-weight:700;display:flex;align-items:center;justify-content:center}

/* footer */
.foot-brand{left:90px;top:3848px;display:flex;align-items:center;gap:12px}
.foot-brand .brand-dot{width:52px;height:52px;background:var(--white)}
.foot-brand .brand-name{font-size:40px;color:var(--white)}
.foot-claim{left:552px;top:3838px;width:560px;font-size:19px;line-height:1.4;color:#e6e6e6;text-transform:uppercase}
.foot-earn{left:552px;top:3914px;font-size:19px;font-weight:700;color:var(--white)}
.foot-nav{left:84px;top:4004px;display:flex;gap:54px;font-size:13px;color:var(--white)}
.btn-contact{left:552px;top:3994px;width:115px;height:38px;background:var(--amber);color:#1a1a1a;font-size:13px;display:flex;align-items:center;justify-content:center}
.social{top:3994px;width:40px;height:40px;border:1.5px solid var(--white)}
.foot-rule{left:84px;top:4075px;width:1033px;height:1px;background:#555}
.copy{top:4102px;width:1200px;text-align:center;font-size:13px;color:#cfcfcf}
.copy b{color:var(--white);font-weight:700}
</style>
</head>
<body>

<header>
  <div class="abs brand"><div class="brand-dot"></div><div class="brand-name">DebtHarbor</div></div>
  <nav class="abs nav"><span>Home</span><span class="active">How It Works</span><span>About US</span><span>Contact</span></nav>
  <div class="abs btn-login">Login</div>
  <div class="abs btn-pm">Property Managers Login</div>
</header>

<h1 class="abs page-title">How It Works</h1>
<p class="abs page-sub">Debt Collection Process</p>

<svg class="abs connectors" width="1200" height="2900" viewBox="0 0 1200 2900" fill="none">
  <path d="M250 596V680H950V767M950 1050V1134H250V1220M250 1503V1587H950V1674M950 1957V2041H250V2128M250 2411V2494H950V2581"
        stroke="var(--line)" stroke-width="1.5" stroke-dasharray="6 6"/>
</svg>

<!-- step 1 -->
<div class="abs photo" style="left:84px;top:313px;background:linear-gradient(135deg,#c9a27a,#8a6748 60,#3b3f4a)" role="img" aria-label="Laptop on a wooden desk showing a website"></div>
<div class="abs step-text" style="left:494px;top:370px">
  <div class="badge">STEP 1</div>
  <h2 class="step-title">Transfer accounts to DebtHarbor</h2>
  <p class="step-body">Lorem Ipsum is simply dummy text of the printing and typesetting industry. Lorem Ipsum has been the industry's standard dummy text ever since the 1500s, when an unknown printer took a galley of type and scrambled it to make a type specimen book</p>
</div>

<!-- step 2 -->
<div class="abs photo" style="left:783px;top:767px;background:linear-gradient(135deg,#e7e9ee,#c8ccd4 55%,#6b5a52)" role="img" aria-label="Agent on the phone at a laptop in an office"></div>
<div class="abs step-text" style="left:84px;top:804px">
  <div class="badge">STEP 2</div>
  <h2 class="step-title">We contact your past resident before<br>they are delinquent</h2>
  <p class="step-body">Lorem Ipsum is simply dummy text of the printing and typesetting industry. Lorem Ipsum has been the industry's standard dummy text ever since the 1500s, when an unknown printer took a galley of type and scrambled it to make a type specimen book</p>
</div>

<!-- step 3 -->
<div class="abs photo" style="left:84px;top:1220px;background:linear-gradient(135deg,#dfe4ea,#a8b6c4 50%,#2c2c30)" role="img" aria-label="Customer paying by phone at a card reader"></div>
<div class="abs step-text" style="left:494px;top:1277px">
  <div class="badge">STEP 3</div>
  <h2 class="step-title">We offer convenient payment platforms</h2>
  <p class="step-body">Lorem Ipsum is simply dummy text of the printing and typesetting industry. Lorem Ipsum has been the industry's standard dummy text ever since the 1500s, when an unknown printer took a galley of type and scrambled it to make a type specimen book</p>
</div>

<!-- step 4 -->
<div class="abs photo" style="left:778px;top:1674px;background:linear-gradient(135deg,#c5c3bd,#6f6a62 55%,#1e2126)" role="img" aria-label="Collector on the phone at his computer"></div>
<div class="abs step-text" style="left:84px;top:1711px">
  <div class="badge">STEP 4</div>
  <h2 class="step-title">Intense collections begins once<br>delinquent</h2>
  <p class="step-body">Lorem Ipsum is simply dummy text of the printing and typesetting industry. Lorem Ipsum has been the industry's standard dummy text ever since the 1500s, when an unknown printer took a galley of type and scrambled it to make a type specimen book</p>
</div>

<!-- step 5 -->
<div class="abs photo" style="left:84px;top:2128px;background:linear-gradient(135deg,#8c6e5c,#d9d9d6 50%,#f1f1ef)" role="img" aria-label="Person typing on a laptop showing charts"></div>
<div class="abs step-text" style="left:494px;top:2168px">
  <div class="badge">STEP 5</div>
  <h2 class="step-title">Credit reporting and legal action<br>when possible</h2>
  <p class="step-body">Lorem Ipsum is simply dummy text of the printing and typesetting industry. Lorem Ipsum has been the industry's standard dummy text ever since the 1500s, when an unknown printer took a galley of type and scrambled it to make a type specimen book</p>
</div>

<!-- step 6 -->
<div class="abs photo" style="left:778px;top:2581px;background:linear-gradient(135deg,#dfe3ea,#7b5a45 50%,#3a2a22)" role="img" aria-label="Two people shaking hands"></div>
<div class="abs step-text" style="left:84px;top:2618px">
  <div class="badge">STEP 6</div>
  <h2 class="step-title">Continued collection attempts<br>throughout the lifecycle of the account</h2>
  <p class="step-body">Lorem Ipsum is simply dummy text of the printing and typesetting industry. Lorem Ipsum has been the industry's standard dummy text ever since the 1500s, when an unknown printer took a galley of type and scrambled it to make a type specimen book</p>
</div>

<!-- connector nodes -->
<div class="abs node" style="left:250px;top:596px"><span></span></div>
<div class="abs node" style="left:950px;top:767px"><span></span></div>
<div class="abs node" style="left:950px;top:1050px"><span></span></div>
<div class="abs node" style="left:250px;top:1220px"><span></span></div>
<div class="abs node" style="left:250px;top:1503px"><span></span></div>
<div class="abs node" style="left:950px;top:1674px"><span></span></div>
<div class="abs node" style="left:950px;top:1957px"><span></span></div>
<div class="abs node" style="left:250px;top:2128px"><span></span></div>
<div class="abs node" style="left:250px;top:2411px"><span></span></div>
<div class="abs node" style="left:950px;top:2581px"><span></span></div>

<!-- painless process -->
<section class="abs dark"></section>
<h2 class="abs dark-title">Painless Process</h2>
<p class="abs dark-lead">You need a simple but effective approach to your accounts receivable, and you need it fast. Our debt recovery services make it easy to pick a product, securely place accounts, and start to improve the financial outcomes.</p>

<div class="abs card" style="left:84px">
  <div class="card-icon">
    <svg width="48" height="48" viewBox="0 0 48 48" fill="var(--amber)">
      <rect x="4" y="24" width="18" height="20" rx="4"/><rect x="26" y="4" width="18" height="20" rx="4"/>
      <path d="M6 18V10a6 6 0 0 1 6-6h6" stroke="var(--amber)" stroke-width="4" fill="none" stroke-linecap="round"/>
      <path d="M42 30v8a6 6 0 0 1-6 6h-6" stroke="var(--amber)" stroke-width="4" fill="none" stroke-linecap="round"/>
    </svg>
  </div>
  <p class="card-text">We integrate with most property management software.</p>
</div>
<div class="abs card" style="left:434px">
  <div class="card-icon">
    <svg width="48" height="48" viewBox="0 0 48 48">
      <rect x="4" y="4" width="40" height="40" rx="10" fill="var(--amber)"/>
      <path d="M18 12v24M30 12v24" stroke="var(--circle-gray)" stroke-width="3" stroke-linecap="round"/>
      <rect x="14" y="26" width="8" height="6" rx="2" fill="var(--circle-gray)"/><rect x="26" y="16" width="8" height="6" rx="2" fill="var(--circle-gray)"/>
    </svg>
  </div>
  <p class="card-text">Our roll out process is simple, we do the heavy lifting so you can focus on managing your properties.</p>
</div>
<div class="abs card" style="left:786px">
  <div class="card-icon">
    <svg width="48" height="48" viewBox="0 0 48 48">
      <path d="M4 24c6-10 13-14 20-14s14 4 20 14c-6 10-13 14-20 14S10 34 4 24z" fill="var(--amber)"/>
      <circle cx="24" cy="24" r="7" fill="none" stroke="var(--circle-gray)" stroke-width="3"/>
    </svg>
  </div>
  <p class="card-text">DebtHarbor's custom reporting system allows you to decide what you want to see and when you want to see it.</p>
</div>

<div class="abs btn-start">Get Started Now</div>

<!-- footer -->
<footer>
  <div class="abs foot-brand"><div class="brand-dot"></div><div class="brand-name">DebtHarbor</div></div>
  <p class="abs foot-claim">Let DebtHarbor earn your business, if we don't get you paid we don't charge you anything</p>
  <p class="abs foot-earn">We Want To Earn Your Business</p>
  <nav class="abs foot-nav"><span>Home</span><span>How It Works</span><span>Schedule Demo</span><span>About US</span></nav>
  <div class="abs btn-contact">Contact Us</div>
  <div class="abs social" style="left:916px" aria-label="Social link"></div>
  <div class="abs social" style="left:970px" aria-label="Social link"></div>
  <div class="abs social" style="left:1023px" aria-label="Social link"></div>
  <div class="abs social" style="left:1077px" aria-label="Social link"></div>
  <div class="abs foot-rule"></div>
  <p class="abs copy">©2022 All rights reserved by <b>DebtHarbor</b> &nbsp;•&nbsp; Privacy Policy &nbsp;•&nbsp; Term Conditions</p>
</footer>

</body>
</html>
```